Bright Harbor Motors Business Card

Would like a cutting edge / high end Automotive Business card design. Please see current card which is old and dated. Would like to maintain the Bright Harbor Motors logo and same information (address, website, etc).

See our website for the look and feel of what we offer - www.brightharbormotors.example

Target Market(s)

Upper class car buyers

Contact Information for Business Card

Modern high end business card design

Requirements
Nice to have
• Carbon Fiber look background

```html
<!DOCTYPE html>
<html lang="en">
<head>
<meta charset="utf-8">
<title>Bright Harbor Motors Business Card</title>
<link href="https://fonts.googleapis.com/css2?family=Cinzel:wght@700&family=Merriweather:ital@1&family=Handlee&family=Roboto:wght@400;500&display=swap" rel="stylesheet">
<style>
  :root {
    --page: #3a3d42;
    --carbon-dark: #0d0d0e;
    --carbon-mid: #222325;
    --red: #e5232a;
    --red-deep: #a8141a;
    --silver: #e4e6e8;
    --white: #ffffff;
    --gold: #ffd21f;
  }
  * { margin: 0; padding: 0; box-sizing: border-box; }
  html, body { width: 1200px; height: 900px; overflow: hidden; background: var(--page); }
  .sheet {
    width: 1200px; height: 900px;
    display: flex; flex-direction: column; align-items: center; justify-content: center; gap: 40px;
  }
  .card {
    position: relative; width: 700px; height: 400px; overflow: hidden;
    background: radial-gradient(ellipse at 40% 30%, var(--carbon-mid), var(--carbon-dark) 75%);
  }
  .card svg.swoop { position: absolute; inset: 0; }
  .brand {
    position: absolute; font-family: "Cinzel", serif; font-weight: 700;
    color: var(--silver); text-align: center; line-height: 1.05; letter-spacing: 1px; white-space: nowrap;
  }
  .brand::after {
    content: ""; display: block; width: 100%; height: 2px; margin-top: 8px; background: var(--silver);
  }
  /* front */
  .front .brand { left: 30px; top: 20px; width: 260px; font-size: 28px; }
  .car-photo {
    position: absolute; left: 30px; top: 112px; width: 240px; height: 126px; border-radius: 40% 35% 20% 20%;
    background: radial-gradient(ellipse at 50% 45%, #f0383c, var(--red-deep) 70%, #5a0a0d);
  }
  .person { position: absolute; right: 40px; top: 100px; text-align: right; }
  .person-name { font-family: "Handlee", cursive; font-size: 38px; line-height: 1.2; color: var(--silver); }
  .person-role { font-family: "Handlee", cursive; font-size: 24px; line-height: 1.2; color: var(--red); }
  .contacts {
    position: absolute; right: 28px; top: 264px; list-style: none;
    font-family: "Roboto", sans-serif; font-size: 16px; color: var(--white); text-align: right;
  }
  .contacts li { display: flex; align-items: center; justify-content: flex-end; gap: 10px; height: 24px; }
  .contacts svg { width: 15px; height: 15px; fill: var(--red); flex: none; }
  /* back */
  .back .brand { left: 360px; top: 28px; width: 300px; font-size: 32px; }
  .tagline {
    position: absolute; left: 340px; top: 132px; width: 340px; text-align: center;
    font-family: "Merriweather", serif; font-style: italic; font-size: 17px; line-height: 1.6; color: var(--silver);
  }
  .values {
    position: absolute; left: 28px; top: 268px;
    font-family: "Merriweather", serif; font-style: italic; font-size: 17px; color: var(--white);
  }
  .values .star { color: var(--gold); margin: 0 6px; font-style: normal; font-size: 12px; }
</style>
</head>
<body>
<main class="sheet">
  <section class="card front">
    <svg class="swoop" viewBox="0 0 700 400" aria-hidden="true">
      <path d="M0 250 C 250 250 450 230 700 205 L700 230 C 450 255 250 276 0 278 Z" fill="var(--red)"/>
      <path d="M0 246 C 250 246 450 226 700 201" fill="none" stroke="var(--silver)" stroke-width="5"/>
    </svg>
    <div class="brand">Bright Harbor<br>Motors</div>
    <div class="car-photo" role="img" aria-label="Photo of a red sports car, front three-quarter view"></div>
    <div class="person">
      <div class="person-name">Dana Whitlow</div>
      <div class="person-role">Owner</div>
    </div>
    <ul class="contacts">
      <li>415.555.0147 <svg viewBox="0 0 24 24"><path d="M6.6 10.8a15 15 0 0 0 6.6 6.6l2.2-2.2a1 1 0 0 1 1-.25 11 11 0 0 0 3.6.6 1 1 0 0 1 1 1V20a1 1 0 0 1-1 1A17 17 0 0 1 3 4a1 1 0 0 1 1-1h3.5a1 1 0 0 1 1 1 11 11 0 0 0 .6 3.6 1 1 0 0 1-.25 1z"/></svg></li>
      <li>415.555.0182 <svg viewBox="0 0 24 24"><path d="M6 3h10v5H6zM4 9h16a2 2 0 0 1 2 2v6h-4v4H6v-4H2v-6a2 2 0 0 1 2-2zm4 7v3h8v-3z"/></svg></li>
      <li>dana@brightharbormotors.example <svg viewBox="0 0 24 24"><path d="M2 5h20v14H2zm2 2v.5l8 5 8-5V7z"/></svg></li>
      <li>www.brightharbormotors.example <svg viewBox="0 0 24 24"><circle cx="12" cy="12" r="10"/></svg></li>
      <li>1180 Meridian Ave #B, Lakeport, CA 94000 <svg viewBox="0 0 24 24"><path d="M12 2a7 7 0 0 1 7 7c0 5-7 13-7 13S5 14 5 9a7 7 0 0 1 7-7zm0 4a3 3 0 1 0 0 6 3 3 0 0 0 0-6z"/></svg></li>
    </ul>
  </section>

  <section class="card back">
    <svg class="swoop" viewBox="0 0 700 400" aria-hidden="true">
      <path d="M0 150 C 220 150 400 250 480 400 L0 400 Z" fill="var(--red)"/>
      <path d="M0 143 C 228 143 412 245 494 400" fill="none" stroke="var(--silver)" stroke-width="7"/>
    </svg>
    <div class="brand">Bright Harbor<br>Motors</div>
    <p class="tagline">Offering Consignment Sales of Luxury<br>and Exotic Sports Cars</p>
    <p class="values">Quality<span class="star">★</span>Integrity<span class="star">★</span>Service</p>
  </section>
</main>
</body>
</html>
```